Zorvo Salsa label for 16oz jar

We need a design for a label for a 16oz glass jar for salsa (dimensions in inches- 2.75 x9.5). Name of salsa is “Zorvo Salsa” and needs to include a place for medium or hot for the different flavors. Looking for bright Fiesta colors but a mature look. Attached is an image of the coloring scheme we like. There will need to be nutrition facts on one end and a description of the product/flavor on the other side of the label. Ultimately at this point looking for brand design.

```html
<!DOCTYPE html>
<html lang="en">
<head>
<meta charset="utf-8">
<title>Zorvo Salsa – Jar Label</title>
<link href="https://fonts.googleapis.com/css2?family=Fresca&family=Open+Sans:wght@400;600&display=swap" rel="stylesheet">
<style>
  :root {
    --canvas: #ffffff;
    --red: #d8141c;
    --text: #3a2a10;
    --orange: #f1a400;
    --orange-deep: #eea000;
    --yellow: #f6e21a;
    --cream: #fdf0c6;
    --pale: #fbe9b0;
    --guac: #9cb84a;
    --sauce: #a8242a;
    --hero-red: #d9342a;
    --hero-light: #f3e6c8;
  }
  * { margin: 0; padding: 0; box-sizing: border-box; }
  html, body { width: 877px; height: 1200px; overflow: hidden; background: var(--canvas); }
  body { position: relative; font-family: "Open Sans", sans-serif; color: var(--text); }

  .label {
    position: absolute; left: 20px; top: 478px;
    width: 837px; height: 243px; overflow: hidden;
    box-shadow: 0 4px 14px rgba(0,0,0,0.18);
  }
  .panel { position: absolute; top: 0; height: 100%; }
  .panel--flavours { left: 0; width: 278px; background: linear-gradient(90deg, var(--orange) 0%, var(--pale) 45%, var(--cream) 100%); }
  .panel--brand { left: 278px; width: 278px; background: radial-gradient(ellipse at 50% 40%, #f9f36a 0%, var(--yellow) 35%, #f4c300 80%, var(--orange) 100%); }
  .panel--info { left: 556px; width: 281px; background: linear-gradient(90deg, #f6c800 0%, var(--orange) 60%, var(--orange-deep) 100%); }

  .heading {
    position: absolute; font-family: "Fresca", sans-serif; font-size: 21px; line-height: 1;
    color: var(--red); white-space: nowrap;
    text-shadow: 1px 0 #fff, -1px 0 #fff, 0 1px #fff, 0 -1px #fff, 1px 1px #fff, -1px -1px #fff, 1px -1px #fff, -1px 1px #fff;
  }
  .rule { position: absolute; height: 1px; background: var(--red); }

  .flavour-list { position: absolute; left: 20px; list-style: none; font-size: 5.6px; line-height: 1.4; }
  .flavour-list li { position: relative; padding-left: 13px; margin-bottom: 4px; }
  .flavour-list li::before { content: "×"; position: absolute; left: 0; top: -2px; color: var(--red); font-size: 9px; font-weight: 600; }

  .photo { position: absolute; border-radius: 8px; }
  .photo--guac { left: 181px; top: 24px; width: 72px; height: 54px; background: linear-gradient(180deg, var(--guac) 0%, #e9ecdc 100%); }
  .photo--sauce { left: 178px; top: 154px; width: 78px; height: 56px; background: linear-gradient(180deg, var(--sauce) 0%, #ece4dc 100%); }
  .photo--hero { left: 28px; top: 118px; width: 213px; height: 118px; background: linear-gradient(90deg, var(--hero-red) 0%, #e8603a 50%, var(--hero-light) 100%); }

  .brand-name {
    position: absolute; left: 0; top: 24px; width: 100%; text-align: center;
    font-family: "Fresca", sans-serif; font-size: 44px; font-weight: 400; line-height: 1; color: var(--red);
  }

  .info-copy { position: absolute; left: 22px; width: 240px; font-size: 5.6px; line-height: 1.45; color: #3a2200; }
  .fact-list { position: absolute; left: 22px; top: 82px; list-style: none; font-size: 9.6px; line-height: 1; color: #3a2200; }
  .fact-list li { display: flex; align-items: center; margin-bottom: 6.5px; }
  .fact-list li::before { content: ""; width: 10px; height: 10px; border-radius: 50%; background: var(--red); margin-right: 14px; flex: none; }
</style>
</head>
<body>
  <section class="label" aria-label="Zorvo Salsa jar label">
    <div class="panel panel--flavours">
      <h2 class="heading" style="left:20px; top:25px;">Medium flavours</h2>
      <div class="rule" style="left:20px; top:52px; width:153px;"></div>
      <div class="photo photo--guac" role="img" aria-label="Photo of a bowl of green medium salsa"></div>
      <ul class="flavour-list" style="top:60px; width:230px;">
        <li style="width:160px;">Lorem Ipsum is simply dummy text of the printing and typesetting industry. Lorem Ipsum has been the industry's standard</li>
        <li>Lorem Ipsum is simply dummy text of the printing and typesetting industry. Lorem Ipsum has been the industry's standard</li>
        <li>Lorem Ipsum is simply dummy text of the printing and typesetting industry. Lorem Ipsum has been the industry's standard</li>
        <li>Lorem Ipsum is simply dummy text of the printing and typesetting industry. Lorem Ipsum has been the industry's standard</li>
      </ul>
      <h2 class="heading" style="left:20px; top:164px;">Hot flavours</h2>
      <div class="rule" style="left:20px; top:190px; width:153px;"></div>
      <div class="photo photo--sauce" role="img" aria-label="Photo of a bowl of red hot salsa"></div>
      <ul class="flavour-list" style="top:197px; width:230px;">
        <li style="width:150px;">Lorem Ipsum is simply dummy text of the printing and typesetting industry.</li>
        <li>Lorem Ipsum is simply dummy text of the printing and typesetting industry. Lorem Ipsum has been the industry's standard</li>
      </ul>
    </div>

    <div class="panel panel--brand">
      <h1 class="brand-name">Zorvo<br>Salsa</h1>
      <div class="photo photo--hero" role="img" aria-label="Photo of a red pepper beside a bowl of salsa with a tortilla chip"></div>
    </div>

    <div class="panel panel--info">
      <h2 class="heading" style="left:22px; top:25px;">Nutrition facts</h2>
      <div class="rule" style="left:22px; top:52px; width:240px;"></div>
      <p class="info-copy" style="top:62px;">Lorem Ipsum is simply dummy text of the printing and typesetting industry. Lorem Ipsum has been the industry's standard dummy text ever since the 1500s,</p>
      <ul class="fact-list">
        <li>Lorem Ipsum is simply dummy text</li>
        <li>Lorem Ipsum is simply dummy text</li>
        <li>Lorem Ipsum is simply dummy text</li>
      </ul>
      <h2 class="heading" style="left:22px; top:152px;">Product description</h2>
      <div class="rule" style="left:22px; top:181px; width:240px;"></div>
      <p class="info-copy" style="top:190px;">Lorem Ipsum is simply dummy text of the printing and typesetting industry. Lorem Ipsum has been the industry's standard dummy text ever since the 1500s, when an unknown printer took a galley of type and scrambled it to make a type specimen book. It has survived not only five centuries, but also the leap into electronic typesetting, remaining essentially unchanged.</p>
    </div>
  </section>
</body>
</html>
```